Property letting UK website

I need a web design for a new Property letting company in the UK. I already have a logo that was produced and won by a pixel harbor logo designer last week.

I like modern designs and require ease of functionality and usage. I already have a domain name registered so need to be able to link to that domain.

Regards,

Miles.

Target Market(s)

UK property

Industry/Entity Type

It Company

Number of Pages Required

5+ page

Requirements
Must have
• Home page, Current properties to let page, About us page, Contact us page, Testimonials page and ability to link to chirpnet and Friendlane account.

```html
<!DOCTYPE html>
<html lang="en">
<head>
<meta charset="utf-8">
<title>Nestwell Lettings</title>
<link rel="stylesheet" href="https://fonts.googleapis.com/css2?family=Oswald:wght@400;500&family=Arimo:wght@400;700&display=swap">
<style>
  :root{
    --page-bg:#1f2130;
    --header-bg:#46484e;
    --nav-bg:#393b44;
    --nav-active:#0aa9e6;
    --accent:#17b4ef;
    --section-dark:#4a4c54;
    --text-light:#ffffff;
    --text-muted:#c9cace;
    --section-light:#f4f4f4;
    --heading-dark:#2a2b30;
    --body-dark:#666;
  }
  *{margin:0;padding:0;box-sizing:border-box}
  html,body{width:1200px;height:1200px;overflow:hidden}
  body{background:var(--page-bg);font-family:Arimo,Arial,sans-serif;position:relative}
  .site{position:absolute;left:98px;top:37px;width:1020px;height:1163px;overflow:hidden}
  .header{position:absolute;left:0;top:0;width:1020px;height:134px;background:var(--header-bg)}
  .brand{position:absolute;left:40px;top:58px;display:flex;align-items:center;gap:10px;color:#e9ecef;font-family:Arimo,Arial,sans-serif;font-size:34px;font-weight:400;letter-spacing:1px}
  .brand-mark{width:16px;height:16px;background:var(--accent)}
  .social{position:absolute;right:40px;top:73px;display:flex;gap:6px}
  .social span{width:24px;height:24px;border-radius:3px;display:block}
  .nav{position:absolute;left:0;top:134px;width:1020px;height:50px;background:var(--nav-bg)}
  .nav ul{list-style:none;display:flex;position:absolute;left:40px;top:0;height:50px}
  .nav li{height:50px;line-height:50px;padding:0 20px;color:var(--text-light);font-size:15px;border-right:1px solid #2e3038}
  .nav li.active{background:var(--nav-active);border-right:none}
  .search{position:absolute;left:779px;top:11px;width:200px;height:29px;background:#5b5d64;border-radius:3px;color:#e6e6e6;font-size:13px;font-style:italic;line-height:29px;padding-left:6px}
  .hero{position:absolute;left:-1px;top:186px;width:1021px;height:474px;background:linear-gradient(160deg,#b9c6cf 0%,#e7e7e3 35%,#8c8c82 62%,#4e5a3a 85%,#6d8a3c 100%)}
  .hero-progress{position:absolute;left:-1px;top:660px;width:1021px;height:4px;background:#2a2c33}
  .hero-progress i{display:block;width:340px;height:4px;background:var(--nav-active)}
  .caption{position:absolute;left:519px;top:454px;width:460px;height:160px;background:rgba(40,40,44,.72);border-radius:8px;padding:24px 30px}
  .caption-pointer{position:absolute;left:30px;top:0}
  .caption h2{font-family:Oswald,sans-serif;font-weight:400;font-size:38px;color:#fff;line-height:42px}
  .caption p{margin-top:10px;font-size:14px;line-height:20px;color:#cfcfcf}
  .caption a{color:var(--accent);text-decoration:none}
  .styles{position:absolute;left:0;top:664px;width:1020px;height:299px;background:var(--section-dark)}
  .section-title{font-family:Oswald,sans-serif;font-weight:400;font-size:15px;color:#fff;position:absolute;left:39px;top:24px;text-transform:uppercase}
  .cards{position:absolute;left:39px;top:69px;display:flex;gap:20px}
  .card{width:220px}
  .card-photo{width:220px;height:120px}
  .card p{margin-top:18px;color:#fff;font-size:12px;line-height:20px}
  .card a{display:block;margin-top:1px;color:var(--accent);font-size:11px;text-decoration:none}
  .lower{position:absolute;left:0;top:963px;width:1020px;height:200px;background:linear-gradient(#fff,var(--section-light))}
  .lower h3{font-family:Oswald,sans-serif;font-weight:400;font-size:20px;color:var(--heading-dark);position:absolute;top:40px}
  .offer{position:absolute;top:100px;width:260px;height:100px}
  .news-date{position:absolute;left:681px;top:99px;width:64px;height:64px;border-radius:5px;background:linear-gradient(#8e9297,#6b6f74);color:#fff;text-align:center;font-size:13px;line-height:20px;padding-top:12px;box-shadow:0 1px 3px rgba(0,0,0,.3)}
  .news-title{position:absolute;left:758px;top:112px;width:220px;font-size:12px;font-weight:700;color:var(--heading-dark);line-height:20px;text-transform:uppercase}
  .news-text{position:absolute;left:758px;top:162px;width:215px;font-size:12px;color:var(--body-dark);line-height:20px}
</style>
</head>
<body>
<div class="site">
  <header class="header">
    <div class="brand"><span class="brand-mark"></span>Nestwell Lettings</div>
    <div class="social">
      <span style="background:#c4302b" role="img" aria-label="Video channel"></span>
      <span style="background:#d34836" role="img" aria-label="Social profile"></span>
      <span style="background:#f08a24" role="img" aria-label="News feed"></span>
      <span style="background:#3cb12c" role="img" aria-label="Share"></span>
      <span style="background:#3ea9dd" role="img" aria-label="chirpnet"></span>
      <span style="background:#3b5998" role="img" aria-label="Friendlane"></span>
    </div>
  </header>
  <nav class="nav">
    <ul>
      <li class="active">HOME</li><li>SERVICES</li><li>PROPERTY</li><li>ABOUT</li><li>NEWS</li><li>CONTACT US</li>
    </ul>
    <div class="search">Search</div>
  </nav>
  <div class="hero" role="img" aria-label="Photo of a white modern two-storey house with a timber pergola terrace and lawn"></div>
  <div class="caption">
    <svg class="caption-pointer" width="32" height="16" viewBox="0 0 32 16"><path d="M0 0H32L16 16Z" fill="#17b4ef"/></svg>
    <h2>Lorem</h2>
    <p>Lorem ipsum dolor sit amet, consectetuer adipiscing elit, sed diam nonummy nibh euismod tincidunt <a href="#">ut laoreet dolore</a> magna aliquam erat volutpat.</p>
  </div>
  <div class="hero-progress"><i></i></div>
  <section class="styles">
    <h2 class="section-title">Apartment Styles</h2>
    <div class="cards">
      <div class="card"><div class="card-photo" role="img" aria-label="Photo of a white modern kitchen" style="background:linear-gradient(135deg,#e8e8e6,#7a746c 60%,#2a2624)"></div><p>Lorem ipsum dolor amet, consectetuer adipiscing elit.</p><a href="#">Lorem ipsum dolor...</a></div>
      <div class="card"><div class="card-photo" role="img" aria-label="Photo of an open-plan concrete living space" style="background:linear-gradient(135deg,#d6d6d2,#8e8a80 55%,#5b4a38)"></div><p>Sed diam nonummy nibh euismod tincidunt ut laoreet dolore.</p><a href="#">Consectetuer adipiscing. Maecenas...</a></div>
      <div class="card"><div class="card-photo" role="img" aria-label="Photo of a concrete courtyard with glass walls" style="background:linear-gradient(135deg,#efefec,#a9a79f 50%,#3b3a36)"></div><p>Ut wisi enim ad minim veniam, quis nostrud exerci tation.</p><a href="#">Sed diam nonummy....</a></div>
      <div class="card"><div class="card-photo" role="img" aria-label="Photo of a covered terrace with a garden view" style="background:linear-gradient(135deg,#2e2c2a,#8c9a9e 50%,#4c6a3a)"></div><p>Consectetuer adipiscing elit, sed diam nonummy nibh euismod.</p><a href="#">Dolore magna aliquam....</a></div>
    </div>
  </section>
  <section class="lower">
    <h3 style="left:39px">LATEST OFFERS</h3>
    <div class="offer" role="img" aria-label="Photo of a modern concrete house" style="left:39px;background:linear-gradient(160deg,#8a8a6a,#d8d8d4 50%,#5a4a40)"></div>
    <div class="offer" role="img" aria-label="Photo of a terrace with mountain view" style="left:359px;background:linear-gradient(160deg,#c8ccd0,#6c6a64 60%,#4a3a2c)"></div>
    <h3 style="left:679px">NEWS &amp; EVENTS</h3>
    <div class="news-date">28 Jun<br>2014</div>
    <div class="news-title">Lorem ipsum dolor amet, consectetuer adipiscing elit.</div>
    <div class="news-text">Lorem ipsum dolor sit amet. Curabitur turpis ante, mollis ut pharetra at,</div>
  </section>
</div>
</body>
</html>
```